Nine Quiet Hours
Business Cards & Letterhead for Sleep Therapist - Health
Business Cards & Letterhead for Sleep Therapist
Professional
Nola J. Barnes, MA, RPSGT, RST, RCC
Founder - Sleep Therapist
4862 Fenwick Avenue, Suite 214 Toronto, ON M6P 2K8
855.52Hushh (855.527.3381)
nola@ninequiethours.example
www.ninequiethours.example www.nineq-hours.example
Front of card should be logo with the tagline "Sleep Consultants and Coaching" on mainly white background, and contact information as provided. I have a few versions of my logo -- I'd like to see both mocked up.
Dark background (black, navy or midnight blue) logo with the tagline "bright ideas for better sleep" & web addresses
jlbarnes jlbarnes
Sincerely, thank you to all the designers who submitted to my project ... I am so pleased with the quality of work.
Hello Designers, I'd appreciate not seeing full stationary design submissions until a business card layout you have submitted has been narrowed to a finalist. There are so many great and unique designs to review ... your time and mine is valuable. So, I will request to see the stationary package options from you when I have selected a business card design of yours that is remaining as one of my finalists. thank you!
Great start! Wow. Thank you for the submissions so far ... general feedback for now, with private feedback to follow soon: 1) please don't merge the two logo concepts (with rare exception - if you have stars on a design now that did this, you've done a unique job that somehow is working for me) The light blue sheep with white and black is one complete look. The yellow moon-bulb with white and midnight blue/navy or black is another complete look. I hope to see/have these two versions of the winning design layout. 2) the light blue as a full colour background for the back of the card doesn't work. I prefer black background with the sheep design on the back of the card. 3) do not use the Hushh for the toll free phone number just the numbers 855.527.3381 and please be sure to denote this as 'toll free' or TF. 4) please make sure both web addresses appear on the card ... if one is used on the front, the other must appear on the back. Or both can appear on the back only ... but both must appear. 5) both logo designs need the tagline "Sleep Coach and Consulting" (no quotation marks though) on the front of the card ... and "bright ideas for better sleep" (all lower case, no quotation marks) on the back of the card. Cheers! I'll do a fresh round of star ratings shortly
I'm open to creative interpretation of my directions ... ie. Logo on the back can be just an element of same (moon-bulb, sheep), larger watermark, etc.? The tagline does not have to reside just under the logo ... Although the front of the cards should be light background & back dark background I don't mind some of the creative touches that tie the sides together more artistically. You're the pros, so I look forward to seeing what is submitted!

```html
<!DOCTYPE html>
<html lang="en">
<head>
<meta charset="utf-8">
<title>Nine Quiet Hours – Business Card</title>
<link rel="stylesheet" href="https://fonts.googleapis.com/css2?family=Nunito:wght@400;600;700;800&display=swap">
<style>
  :root {
    --stage: #2a2b2d;
    --card-dark: #2c2d30;
    --card-dark-edge: #38393c;
    --card-light: #ffffff;
    --ink: #3a3b3e;
    --ink-soft: #6d6f73;
    --teal: #7fcfcb;
    --teal-deep: #3f8f8c;
    --teal-faint: #3c5557;
    --band: #3a3b3e;
    --muted: #a7a9ad;
  }
  * { box-sizing: border-box; margin: 0; padding: 0; }
  html, body { width: 1200px; height: 751px; overflow: hidden; }
  body {
    background: var(--stage);
    font-family: "Nunito", Arial, sans-serif;
    position: relative;
  }
  .card {
    position: absolute;
    top: 221px;
    width: 540px;
    height: 309px;
    border-radius: 14px;
    overflow: hidden;
  }
  .card--back {
    left: 40px;
    background: linear-gradient(160deg, var(--card-dark-edge), var(--card-dark) 60%);
  }
  .card--front {
    left: 620px;
    background: var(--card-light);
  }
  .sheep-mark {
    position: absolute;
    border-radius: 50%;
  }
  .card--back .sheep-mark {
    left: 36px; top: 64px; width: 180px; height: 180px;
    background: radial-gradient(circle at 50% 45%, #456062, var(--teal-faint) 70%);
  }
  .brand {
    position: absolute;
    left: 250px; top: 112px;
    display: flex; align-items: center; gap: 9px;
    white-space: nowrap;
  }
  .brand__dot {
    width: 26px; height: 26px; border-radius: 50%;
    background: var(--teal);
    flex: none;
  }
  .brand__name {
    font-size: 27px; font-weight: 700; color: #ffffff;
    letter-spacing: -0.3px; line-height: 1;
  }
  .back-tagline {
    position: absolute;
    left: 286px; top: 148px;
    font-size: 11px; font-weight: 600; color: var(--teal);
    letter-spacing: 0.3px; white-space: nowrap;
  }
  .back-web {
    position: absolute;
    left: 252px; top: 176px;
    font-size: 9.5px; color: var(--muted); letter-spacing: 0.1px;
    white-space: nowrap;
  }
  .card--front .sheep-mark {
    left: 350px; top: 34px; width: 150px; height: 150px;
    background: radial-gradient(circle at 50% 45%, #9adcd9, var(--teal) 70%);
  }
  .sheep-rest {
    position: absolute;
    left: 380px; top: 186px; width: 132px; height: 10px;
    border-radius: 5px; background: var(--band);
  }
  .front-tagline {
    position: absolute;
    left: 372px; top: 206px;
    font-size: 10px; font-weight: 700; color: var(--teal-deep);
    letter-spacing: 0.3px; white-space: nowrap;
  }
  .contact { position: absolute; left: 34px; top: 84px; color: var(--ink); }
  .contact__name { font-size: 22px; font-weight: 800; line-height: 1.1; }
  .contact__creds { font-size: 12.5px; font-weight: 700; margin-top: 2px; }
  .contact__role { font-size: 11.5px; font-weight: 700; color: var(--teal-deep); margin-top: 3px; }
  .contact__address { font-size: 10.5px; color: var(--ink-soft); margin-top: 14px; line-height: 1.45; }
  .lines { margin-top: 10px; font-size: 10.5px; color: var(--ink-soft); line-height: 1.6; white-space: nowrap; }
  .line { display: flex; align-items: center; gap: 6px; }
  .line svg { width: 10px; height: 10px; flex: none; }
  .contact--side { left: 196px; top: 178px; }
  .band {
    position: absolute; left: 0; right: 0; bottom: 0; height: 42px;
    background: var(--band);
    display: flex; align-items: center; padding-left: 34px;
    font-size: 11px; color: #ffffff; letter-spacing: 0.2px;
    white-space: nowrap;
  }
  .band .accent { color: var(--teal); }
</style>
</head>
<body>
  <section class="card card--back" aria-label="Card back">
    <div class="sheep-mark" role="img" aria-label="Large faint sheep illustration"></div>
    <div class="brand">
      <span class="brand__dot"></span>
      <span class="brand__name">Nine Quiet Hours</span>
    </div>
    <p class="back-tagline">bright ideas for better sleep</p>
    <p class="back-web">www.ninequiethours.example &nbsp;|&nbsp; www.nineq-hours.example</p>
  </section>

  <section class="card card--front" aria-label="Card front">
    <div class="sheep-mark" role="img" aria-label="Light blue sheep illustration"></div>
    <div class="sheep-rest"></div>
    <p class="front-tagline">Sleep Coach and Consulting</p>

    <div class="contact">
      <p class="contact__name">Nola J. Barnes</p>
      <p class="contact__creds">MA, RPSGT, RST, RCC</p>
      <p class="contact__role">Founder · Sleep Therapist</p>
      <p class="contact__address">4862 Fenwick Avenue,<br>Suite 214 Toronto, ON M6P 2K8</p>
      <div class="lines">
        <p class="line">
          <svg viewBox="0 0 10 10"><path d="M2 1l2 2-1 1.3c.6 1.2 1.5 2.1 2.7 2.7L7 6l2 2-1.3 1.3C4.5 9 1 5.5.7 2.3z" fill="#3f8f8c"/></svg>
          855.527.3381 (TF)
        </p>
        <p class="line">
          <svg viewBox="0 0 10 10"><path d="M2 1l2 2-1 1.3c.6 1.2 1.5 2.1 2.7 2.7L7 6l2 2-1.3 1.3C4.5 9 1 5.5.7 2.3z" fill="#3f8f8c"/></svg>
          905.361.4470
        </p>
      </div>
    </div>

    <div class="contact contact--side">
      <div class="lines">
        <p class="line">
          <svg viewBox="0 0 10 10"><rect x="1" y="2" width="8" height="6" rx="1" fill="#3f8f8c"/></svg>
          F 905.361.4471
        </p>
        <p class="line">
          <svg viewBox="0 0 10 10"><rect x="1" y="2.5" width="8" height="5.5" rx="0.8" fill="none" stroke="#3f8f8c" stroke-width="1.2"/><path d="M1.4 3l3.6 2.6L8.6 3" fill="none" stroke="#3f8f8c" stroke-width="1.1"/></svg>
          nola@ninequiethours.example
        </p>
      </div>
    </div>

    <div class="band">
      <span>www.ninequiethours.example</span>&nbsp;&nbsp;<span class="accent">|</span>&nbsp;&nbsp;<span class="accent">www.nineq-hours.example</span>
    </div>
  </section>
</body>
</html>
```